Business Card for Professional Photographer

I'm looking for an eye catching modern clean design that compliments my logo/ website fonts & colours.
I specialise in architecture, corporate & commercial photography so I'm marketing to professional clients rather than portrait / wedding clients.

I would prefer to not have a solid black design.

My logo brand guide is as follows :

Main front font. : Reislust
Main font colour : #fff
Slogan front font : Ubuntu Bold
Monogram front font : Venti Medium
Container colour : #fff

I need print ready files in pdf .png & .eps formats.

Included in the files below are some screen grabs as reference to font & colours etc.

```html
<!DOCTYPE html>
<html lang="en">
<head>
<meta charset="utf-8">
<title>Still Axis – Business Card</title>
<link rel="stylesheet" href="https://fonts.googleapis.com/css2?family=Lato:wght@300;400;700&display=swap">
<style>
  :root {
    --backdrop: #3b3b3d;
    --card: #17161b;
    --card-edge: #222127;
    --gold: #d6a843;
    --white: #f2f2f2;
    --divider: #3a3940;
  }
  * { margin: 0; padding: 0; box-sizing: border-box; }
  html, body {
    width: 1200px; height: 1015px; overflow: hidden;
    background: var(--backdrop);
    font-family: "Lato", sans-serif;
  }
  .stage {
    width: 1200px; height: 1015px;
    display: flex; flex-direction: column;
    align-items: center; justify-content: center; gap: 44px;
  }
  .card {
    position: relative;
    width: 760px; height: 434px;
    background: var(--card);
    box-shadow: 0 18px 40px rgba(0,0,0,.45);
    overflow: hidden;
  }
  /* back side */
  .card-back .pattern {
    position: absolute; inset: 0;
    background: radial-gradient(ellipse at center, #1d1c22 0%, var(--card) 75%);
  }
  .card-back .brand-mark {
    position: absolute; inset: 0;
    display: flex; align-items: center; justify-content: center; gap: 14px;
  }
  .brand-dot {
    width: 22px; height: 22px; border-radius: 50%;
    border: 2px solid var(--gold);
  }
  .brand-name-gold {
    font-weight: 300; font-size: 26px; letter-spacing: .22em;
    color: var(--gold); text-transform: uppercase;
  }
  /* front side */
  .logo-block {
    position: absolute; left: 58px; top: 208px;
    display: flex; align-items: center; gap: 20px;
  }
  .logo-circle {
    width: 64px; height: 64px; border-radius: 50%;
    border: 3px solid var(--gold);
  }
  .brand-name {
    font-weight: 300; font-size: 27px; letter-spacing: .2em;
    color: var(--white); text-transform: uppercase; line-height: 1;
  }
  .brand-slogan {
    margin-top: 7px;
    font-weight: 700; font-size: 9px; letter-spacing: .14em;
    color: var(--white);
  }
  .divider {
    position: absolute; left: 420px; top: 120px;
    width: 1px; height: 200px; background: var(--divider);
  }
  .contact {
    position: absolute; left: 448px; top: 122px;
    color: var(--white);
  }
  .person-name {
    font-weight: 700; font-size: 25px; color: var(--gold);
    text-transform: uppercase; line-height: 1;
  }
  .person-role { font-size: 17px; margin-top: 2px; }
  .contact-list { list-style: none; margin-top: 10px; }
  .contact-list li {
    display: flex; align-items: center; gap: 8px;
    font-size: 17px; line-height: 26px;
  }
  .contact-list svg { width: 14px; height: 14px; flex: none; }
  .address { font-size: 17px; line-height: 22px; margin-top: 8px; }
</style>
</head>
<body>
<main class="stage">
  <section class="card card-back">
    <div class="pattern" role="img" aria-label="Faint tiled pattern of small camera outlines across the dark card"></div>
    <div class="brand-mark">
      <span class="brand-dot"></span>
      <span class="brand-name-gold">Still Axis</span>
    </div>
  </section>

  <section class="card card-front">
    <div class="logo-block">
      <span class="logo-circle"></span>
      <div>
        <div class="brand-name">Still Axis</div>
        <div class="brand-slogan">Architecture Corporate Commercial</div>
      </div>
    </div>

    <div class="divider"></div>

    <div class="contact">
      <div class="person-name">Marcus Hale</div>
      <div class="person-role">Managing Director</div>
      <ul class="contact-list">
        <li>
          <svg viewBox="0 0 14 14" aria-hidden="true"><path fill="#d6a843" d="M3 1h2l1 3-1.5 1a7 7 0 0 0 4.5 4.5L10 8l3 1v2a2 2 0 0 1-2 2A10 10 0 0 1 1 3a2 2 0 0 1 2-2z"/></svg>
          044-987 210 553
        </li>
        <li>
          <svg viewBox="0 0 14 14" aria-hidden="true"><rect x="1" y="3" width="12" height="8" fill="#d6a843"/><path d="M1 3l6 5 6-5" stroke="#17161b" stroke-width="1.2" fill="none"/></svg>
          hello@stillaxis.studio
        </li>
        <li>
          <svg viewBox="0 0 14 14" aria-hidden="true"><circle cx="7" cy="7" r="6" fill="#d6a843"/><path d="M1 7h12M7 1c-3 3-3 9 0 12M7 1c3 3 3 9 0 12" stroke="#17161b" stroke-width="1" fill="none"/></svg>
          www.stillaxis.studio
        </li>
      </ul>
      <p class="address">17, Harbour Lane<br>Westport, 30918</p>
    </div>
  </section>
</main>
</body>
</html>
```